Simple, Elegant, Clean Homepage Design For Hirevane.com - for job seekers.

Hello, we're going to start this site by posting a project for ONE page of it - the homepage. I've attached a simple wireframe I created and we'll be using logo #1 in the attached PDF.

Anyway, all the wireframe shows is where the elements should be. You'll put in placeholder image(s) where needed. (i.e. The BrightDesk banner.)

We are looking for a simple, clean site - very minimalistic but also one that grabs the eye.

Simple, clean menu across the top...the little links at the bottom...

And in the middle show us some headline styles, subhead styles, body copy font style, and bullets we can use.

As you can see there is also a search tool for employers in the upper right, so we'd like to see your vision of that as well.

Thanks!

Tom

P.S. You can just put in some garbled example text to illustrate fonts and other elements listed in the description.

P.P.S. I just added a new PDF to this project showing some updated tag lines we like with the "hirevane.com/your-name-here" thing we like. See if this can be integrated into your existing designs - or new designs.

Target Market(s)

Job Seekers

Number of Pages Required

1 page

Font styles to use
Sans Serif

Colors
ffffff
0456a4
000000
c5c5c5

Requirements
Must have
• Must be a simple, clean, optimized HTML/CSS design. We are looking for a minimalistic approach, so that we can easily highlight certain features/text/icons with color.
Nice to have
• White background, elegant and "soft" outlines for sections, easy to read font, headline fonts/colors that grab, tasteful bullets.
Should not have
• Complex design
• hard to read fonts
• busy/loud design
• not too serious, not too casual

```html
<!DOCTYPE html>
<html lang="en">
<head>
<meta charset="utf-8">
<title>Hirevane — Homepage</title>
<link href="https://fonts.googleapis.com/css2?family=Nunito+Sans:wght@300;400;600;700;800&display=swap" rel="stylesheet">
<style>
:root{
  --blue:#0456a4;
  --icon:#1d74b8;
  --ink:#1a1a1a;
  --muted:#666;
  --line:#c5c5c5;
  --orange:#f5903d;
  --burnt:#d65a1c;
  --footer:#232323;
  --white:#ffffff;
}
*{box-sizing:border-box;margin:0;padding:0}
html,body{width:898px;height:1200px;overflow:hidden;background:var(--white)}
body{font-family:"Nunito Sans",sans-serif;color:var(--ink);position:relative}
.abs{position:absolute}

/* header */
.brand{left:66px;top:30px;font-size:30px;font-weight:700;color:var(--icon);letter-spacing:-.5px;line-height:1}
.nav{left:262px;top:40px;display:flex;gap:27px;font-size:13.5px;color:#444}
.employers{left:680px;top:12px;font-size:13px;color:#444}
.search{left:599px;top:31px;width:233px;height:36px;border:1px solid #999;border-radius:18px;display:flex;align-items:center;justify-content:space-between;padding:0 16px;font-size:13.5px;color:#333;box-shadow:0 1px 3px rgba(0,0,0,.15)}

/* hero */
.hero{left:0;top:96px;width:898px;height:364px;background:linear-gradient(90deg,#07476a,#0a5a82 60%,#064a6c)}
.video{left:66px;top:133px;width:570px;height:296px;border:2px solid #8fa7b4;background:linear-gradient(90deg,#9aa5ac 0%,#7c8d99 30%,#2d4670 55%,#1c2a3d 100%)}
.play{left:260px;top:120px;width:52px;height:52px;border-radius:50%;background:rgba(20,20,20,.75);border:2px solid #ddd;display:flex;align-items:center;justify-content:center}
.video-title{left:0;width:100%;top:200px;text-align:center;color:var(--white)}
.video-title h1{font-size:29px;font-weight:800;letter-spacing:.5px}
.video-title p{font-size:17px;font-weight:400}
.side{left:643px;top:133px;width:189px;height:296px;background:linear-gradient(180deg,#d9cdbf,#bfae9b);overflow:hidden}
.side-band{left:0;bottom:0;width:100%;height:78px;background:linear-gradient(180deg,#e46a28,var(--burnt));border-top:3px solid rgba(255,255,255,.7);text-align:center;color:var(--white);padding-top:16px}
.side-band h2{font-size:21px;font-weight:600;line-height:1}
.side-band p{font-size:12px;font-weight:600;margin-top:4px}

/* categories */
.cat-title{left:0;width:898px;top:509px;text-align:center;font-size:21.5px;font-weight:400;letter-spacing:.5px}
.cat{top:581px;width:196px;text-align:center}
.cat-icon{width:80px;height:80px;border:1px solid #444;border-radius:50%;margin:0 auto;display:flex;align-items:center;justify-content:center}
.cat h3{font-size:14.5px;font-weight:400;margin-top:12px}
.cat p{font-size:9.8px;color:var(--muted);line-height:14.5px;margin-top:9px;padding:0 14px}
.arrow{top:636px}

/* feature */
.feature{left:0;top:802px;width:898px;height:305px;background:linear-gradient(90deg,#bcd3e6 0%,#d3e2ef 40%,#eaf1f8 65%,#f3f7fb 100%)}
.feature-art{left:0;top:0;width:420px;height:305px;background:radial-gradient(ellipse at 45% 45%,#e8c2aa 0%,#cfdbe7 45%,rgba(211,226,239,0) 75%)}
.feature-copy{left:417px;top:88px;width:440px}
.feature-copy h2{font-size:19.5px;font-weight:400;color:#222;letter-spacing:.2px;white-space:nowrap}
.ticks{list-style:none;margin-top:8px}
.ticks li{font-size:10.5px;color:#444;display:flex;align-items:center;gap:7px;height:20px}
.feature-copy .body{font-size:10.5px;color:#444;line-height:19px;margin-top:6px;width:400px}
.btn{display:inline-block;margin-top:12px;background:var(--orange);color:var(--white);font-size:10.5px;font-weight:600;padding:5px 16px;border-radius:12px}

/* footer */
.footer{left:0;top:1107px;width:898px;height:93px;background:var(--footer);color:var(--white);font-size:12px}
.copy{left:66px;top:41px}
.links{right:74px;top:39px;display:flex;gap:6px}
</style>
</head>
<body>

<header>
  <div class="abs brand">Hirevane</div>
  <nav class="abs nav"><span>About</span><span>Support</span><span>Sign In</span><span>Free Training</span></nav>
  <div class="abs employers">Employers</div>
  <div class="abs search">
    <span>Candidate search</span>
    <svg width="15" height="15" viewBox="0 0 16 16"><circle cx="6.5" cy="6.5" r="5" fill="none" stroke="#222" stroke-width="2.2"/><line x1="10.3" y1="10.3" x2="14.5" y2="14.5" stroke="#222" stroke-width="2.4" stroke-linecap="round"/></svg>
  </div>
</header>

<section class="abs hero"></section>
<div class="abs video" role="img" aria-label="Video still: businessman writing at a desk in an office">
  <div class="abs play"><svg width="20" height="22" viewBox="0 0 20 22"><path d="M3 1 L19 11 L3 21 Z" fill="#fff"/></svg></div>
  <div class="abs video-title"><h1>HIREVANE</h1><p>Neque porro quisquam</p></div>
</div>
<div class="abs side" role="img" aria-label="Photo: woman with headphones taking an online class">
  <div class="abs side-band"><h2>BrightDesk</h2><p>Neque porro quisquam</p></div>
</div>

<h2 class="abs cat-title">POPULAR CATEGORIES</h2>

<svg class="abs arrow" style="left:38px" width="16" height="30" viewBox="0 0 16 30"><polyline points="15,1 1,15 15,29" fill="none" stroke="#888" stroke-width="1.2"/></svg>
<svg class="abs arrow" style="left:844px" width="16" height="30" viewBox="0 0 16 30"><polyline points="1,1 15,15 1,29" fill="none" stroke="#888" stroke-width="1.2"/></svg>

<div class="abs cat" style="left:52px">
  <div class="cat-icon"><svg width="34" height="28" viewBox="0 0 34 28"><polyline points="2,2 2,26 33,26" fill="none" stroke="#1d74b8" stroke-width="3"/><polyline points="7,20 14,12 19,16 29,6" fill="none" stroke="#1d74b8" stroke-width="3"/><path d="M24 4 L31 4 L31 11 Z" fill="#1d74b8"/></svg></div>
  <h3>Accountance</h3>
  <p>It has survived not only five centuries, but also the leap into electronic typesetting, remaining</p>
</div>
<div class="abs cat" style="left:254px">
  <div class="cat-icon"><svg width="32" height="30" viewBox="0 0 32 30"><path d="M16 1 L31 8 L1 8 Z" fill="#1d74b8"/><rect x="2" y="9" width="28" height="3" fill="#1d74b8"/><rect x="5" y="13" width="3" height="10" fill="#1d74b8"/><rect x="11" y="13" width="3" height="10" fill="#1d74b8"/><rect x="18" y="13" width="3" height="10" fill="#1d74b8"/><rect x="24" y="13" width="3" height="10" fill="#1d74b8"/><rect x="1" y="24" width="30" height="4" fill="#1d74b8"/></svg></div>
  <h3>Banking</h3>
  <p>It has survived not only five centuries, but also the leap into electronic typesetting, remaining</p>
</div>
<div class="abs cat" style="left:455px">
  <div class="cat-icon"><svg width="28" height="28" viewBox="0 0 28 28"><path d="M20 2 L26 8 L10 24 L2 26 L4 18 Z" fill="#1d74b8"/><line x1="17" y1="5" x2="23" y2="11" stroke="#fff" stroke-width="1.5"/><line x1="4.5" y1="18.5" x2="9.5" y2="23.5" stroke="#fff" stroke-width="1.5"/></svg></div>
  <h3>Design &amp; Art</h3>
  <p>It has survived not only five centuries, but also the leap into electronic typesetting, remaining</p>
</div>
<div class="abs cat" style="left:652px">
  <div class="cat-icon"><svg width="32" height="28" viewBox="0 0 32 28"><rect x="1" y="1" width="30" height="20" rx="2" fill="#1d74b8"/><rect x="4" y="4" width="24" height="13" fill="#fff"/><rect x="13" y="21" width="6" height="4" fill="#1d74b8"/><rect x="8" y="25" width="16" height="2.5" fill="#1d74b8"/></svg></div>
  <h3>IT Engineer</h3>
  <p>It has survived not only five centuries, but also the leap into electronic typesetting, remaining</p>
</div>

<section class="abs feature">
  <div class="abs feature-art" role="img" aria-label="Photo: hand circling one person icon in a network of blue people icons"></div>
  <div class="abs feature-copy">
    <h2>FIND THE PERFECT JOB AS YOUR PROFILE</h2>
    <ul class="ticks">
      <li><svg width="11" height="11" viewBox="0 0 11 11"><rect x=".5" y=".5" width="10" height="10" fill="none" stroke="#1d74b8"/><polyline points="2.5,5.5 4.8,8 9.5,2.5" fill="none" stroke="#1d74b8" stroke-width="1.6"/></svg>Condimentum eros pretium nam vel magnas nec diam.</li>
      <li><svg width="11" height="11" viewBox="0 0 11 11"><rect x=".5" y=".5" width="10" height="10" fill="none" stroke="#1d74b8"/><polyline points="2.5,5.5 4.8,8 9.5,2.5" fill="none" stroke="#1d74b8" stroke-width="1.6"/></svg>Diam commodo viverra eget leo curabitur diam consequat</li>
      <li><svg width="11" height="11" viewBox="0 0 11 11"><rect x=".5" y=".5" width="10" height="10" fill="none" stroke="#1d74b8"/><polyline points="2.5,5.5 4.8,8 9.5,2.5" fill="none" stroke="#1d74b8" stroke-width="1.6"/></svg>Nam luctus venenatis mauris et luctus sem lacinia et.</li>
    </ul>
    <p class="body">It is a long established fact that a reader will be distracted by the readable content of a page when looking at its layout. The point of using Lorem Ipsum is that</p>
    <span class="btn">Pre-Employment Tests</span>
  </div>
</section>

<footer class="abs footer">
  <div class="abs copy">Copyright © 2017. All Rights Reserved</div>
  <div class="abs links"><span>Contact</span>|<span>Terms</span>|<span>Disclaimer</span>|<span>Privacy</span>|<span>Sign in</span>|<span>Directory</span></div>
</footer>

</body>
</html>
```